Vorental d.o.o. needes a web site design

We are a company dealing with automatic doors, industrial doors, roller shutters, access control systems.
We would like to get a design which is clean and neat, and here are some sites which work with similar products. These designs are some we like, but of course, I am looking for a design which is unique. We usually use grey and red colours, which you can see on www.vorental.ba .
The sites we like are:
http://www.plinsta.com/gb/
http://www.bravidosteel.it/eng/
http://morrowpanelgate.com/

You have to understand, that we have 4 different groups of products, which are main groups. I would like if those 4 groups somehow could be in different colours. (Maybe "zenpoq" colours), in order to separate the groups in some way.

Attached you have web site structure.

If any questions, please contact me.
Edvan

Target Market(s)

Bosnian market. Aluminium and PVC doors and window market, Construction companies, Supermarkets-Retail, Gas stations, Banks, Food industry, Heavy industry.

Industry/Entity Type

It Company

Contact Information for Business Card

I have attached our current business card in PDF. I weould like english on one side, bosnian on other side.

Logo Text

Vorental is the name of the company, our core business is automation!

Number of Pages Required

5+ page

Font styles to use
Sans Serif

Colors
ec1f27
0792cd
9bcb3c
ffc214
ffffff

```html
<!DOCTYPE html>
<html lang="en">
<head>
<meta charset="utf-8">
<title>Vorental d.o.o.</title>
<link href="https://fonts.googleapis.com/css2?family=Roboto:ital,wght@0,400;0,500;0,700;1,400&family=Montserrat:wght@400;600&display=swap" rel="stylesheet">
<style>
:root{
  --red:#ec1f27;--menu-red:#d8283a;--blue:#0792cd;--green:#9bcb3c;--yellow:#ffc214;
  --white:#fff;--page:#f5f5f5;--dark:#474747;--text:#333;--muted:#888;--line:#ddd;
}
*{margin:0;padding:0;box-sizing:border-box}
html,body{width:911px;height:1200px;overflow:hidden}
body{position:relative;background:var(--page);font-family:"Roboto",Arial,sans-serif;color:var(--text)}
.abs{position:absolute}
.header{left:0;top:0;width:911px;height:89px;background:var(--white)}
.header-rule{left:0;top:58px;width:911px;height:1px;background:var(--menu-red)}
.brand{left:148px;top:30px;display:flex;align-items:center;gap:8px;font-size:20px;font-weight:700;color:var(--red);letter-spacing:1px;white-space:nowrap}
.brand-mark{width:14px;height:14px;background:var(--red);flex:none}
.social{right:148px;top:37px;font-size:9px;color:#aaa;letter-spacing:.5px}
.nav{left:489px;top:59px;display:flex;height:30px;font-size:10.5px}
.nav a{color:#333;text-decoration:none;padding:0 14px;line-height:22px}
.nav a.active{background:var(--dark);color:#fff;padding:0 19px;height:30px}
.hero{left:0;top:89px;width:911px;height:339px;background:linear-gradient(180deg,#6f6a66 0%,#a7a5a3 50%,#4a4645 100%)}
.arrow{top:250px;width:18px;height:30px}
.dots{left:434px;top:381px;display:flex;gap:4px}
.dots i{width:8px;height:8px;border:1.5px solid #fff;border-radius:50%}
.dots i.on{background:var(--red);border-color:var(--red)}
.dropdown{left:137px;top:94px;width:637px;height:203px;border-bottom:3px solid #fff;display:flex}
.col{height:200px}
.col1{width:165px;background:var(--dark)}
.col2{width:182px;background:var(--dark)}
.col3{width:290px;background:var(--menu-red);padding-left:15px}
.item{display:flex;justify-content:space-between;align-items:center;height:39px;color:#fff;font-size:10.5px;padding:0 22px 0 31px;border-bottom:1px solid #5a5a5a;margin-right:6px;white-space:nowrap}
.col2 .item{padding:0 14px 0 14px;margin:0 10px 0 0}
.item.on{background:var(--menu-red);border-color:var(--menu-red);margin-right:0}
.col3 .item{padding:0;width:157px;border-color:#f2a0a8}
.intro{left:148px;top:452px;width:616px;height:72px;background:#fff}
.clock{left:22px;top:14px;width:46px;height:46px;border-radius:50%;border:3px solid #333}
.intro-rule{left:90px;top:16px;width:1px;height:40px;background:#ccc}
.intro p{left:106px;top:22px;width:470px;font-size:8.8px;font-style:italic;line-height:16px;color:#555}
.tabs{left:148px;top:524px;display:flex;height:62px}
.tab{color:#fff;padding:18px 16px;font-family:"Montserrat",sans-serif;position:relative}
.tab h3{font-size:9.5px;font-weight:600;letter-spacing:.6px;white-space:nowrap}
.tab span{display:block;font-size:7.5px;font-weight:600;margin-top:7px}
.tab.blue::after{content:"";position:absolute;left:20px;bottom:-6px;border:6px solid transparent;border-top-color:var(--blue);border-bottom:0}
.products{left:148px;top:586px;width:616px;height:190px;background:#fff}
.prod{top:42px;width:158px}
.prod .ph{height:95px}
.prod a{display:block;margin-top:13px;font-size:10.5px;color:var(--blue);text-decoration:none}
.blueline{left:148px;top:777px;width:616px;height:3px;background:var(--blue)}
.card{top:780px;height:90px;background:#fff;padding:8px 20px}
.card h4{font-size:9.5px;font-weight:500}
.card p{font-size:9.5px;line-height:14.5px;margin-top:9px}
.card small{display:block;font-size:6.5px;margin-top:12px;color:#555}
.news{left:567px;top:780px;width:196px;height:84px;border-left:2px solid #ccc;padding-left:9px}
.news .meta{font-size:7px;color:#bbb}
.news p{font-size:10px;line-height:14.5px;color:#555;margin-top:6px}
.news small{display:block;font-size:7.5px;font-style:italic;color:#777;margin-top:12px}
.slider{left:148px;top:890px;width:407px;height:3px;background:#bbb}
.slider i{position:absolute;left:0;top:0;width:103px;height:3px;background:var(--red)}
.slider b{position:absolute;left:99px;top:-4px;width:10px;height:10px;border-radius:50%;border:2px solid var(--red);background:#fff}
.partners{left:148px;top:923px;width:616px;height:121px;background:#fff}
.partners h2{position:absolute;left:0;top:23px;width:616px;text-align:center;font-family:"Montserrat",sans-serif;font-weight:400;font-size:12px;color:#555}
.partners h2::before,.partners h2::after{content:"";display:inline-block;width:36px;height:1px;background:#ccc;vertical-align:middle;margin:0 14px}
.logos{position:absolute;left:40px;top:64px;width:540px;display:flex;justify-content:space-between;font-size:16px;font-weight:500;color:#888}
.footer{top:1060px;font-size:8.5px}
.fcol{border-left:1px solid #ccc;height:110px}
.fcol a{display:block;color:#333;font-weight:500;text-decoration:none;line-height:19.6px}
.contact h5{font-family:"Montserrat",sans-serif;font-weight:400;font-size:11.5px;color:#444;margin-bottom:10px}
.contact div{line-height:19.6px;color:#333}
</style>
</head>
<body>
<header class="abs header"></header>
<div class="abs header-rule"></div>
<div class="abs brand"><span class="brand-mark"></span>vorental d.o.o.</div>
<div class="abs social">Kivo &nbsp; Fabo &nbsp; Pino &nbsp; Lino</div>
<nav class="abs nav"><a>company</a><a class="active">products ⌵</a><a>reference</a><a>contact</a></nav>

<section class="abs hero" role="img" aria-label="Photo of an automatic glass door entrance in a modern lobby"></section>
<svg class="abs arrow" style="left:18px" viewBox="0 0 18 30"><path d="M15 3L3 15l12 12" fill="none" stroke="#fff" stroke-width="2"/></svg>
<svg class="abs arrow" style="left:876px" viewBox="0 0 18 30"><path d="M3 3l12 12L3 27" fill="none" stroke="#fff" stroke-width="2"/></svg>
<div class="abs dots"><i></i><i class="on"></i><i></i><i></i></div>

<div class="abs dropdown">
  <div class="col col1">
    <div class="item on">Automatska Verta <span>›</span></div>
    <div class="item">Industrijska Vrata <span>›</span></div>
    <div class="item">Rolo Vrata <span>›</span></div>
    <div class="item" style="border:0">Kontrola Pristupa <span>›</span></div>
  </div>
  <div class="col col2">
    <div class="item on">Automatska klizna vrata <span>›</span></div>
    <div class="item">Karusel vrata <span>›</span></div>
    <div class="item">Automatike za krilna vrata <span>›</span></div>
    <div class="item" style="border:0">Hermeticka vrata za bolnice <span>›</span></div>
  </div>
  <div class="col col3">
    <div class="item">Klizna vrata</div>
    <div class="item">Klizna teleskopska vrata</div>
    <div class="item">Klizna ukirvljena vrata</div>
  </div>
</div>

<section class="abs intro">
  <div class="abs clock" role="img" aria-label="Round 24/7 service clock icon"></div>
  <div class="abs intro-rule"></div>
  <p class="abs">Find out about Vorental d.o.o services to provide Door Products that helps your business to ensure an effective multi-channel customer engagement.</p>
</section>

<div class="abs tabs">
  <div class="tab" style="width:158px;background:var(--red)"><h3>AUTOMATSKA VRATA</h3><span>view all products</span></div>
  <div class="tab blue" style="width:157px;background:var(--blue)"><h3>INDUSTRIJSKA VRATA</h3></div>
  <div class="tab" style="width:143px;background:var(--green)"><h3>ROLO VRATA</h3><span>view all products</span></div>
  <div class="tab" style="width:158px;background:var(--yellow)"><h3>KONTROLA PRISTUPA</h3><span>view all products</span></div>
</div>

<section class="abs products">
  <div class="abs prod" style="left:52px"><div class="ph" role="img" aria-label="Photo of a steel roller shutter door" style="background:linear-gradient(90deg,#8a7f7c,#bdbdbd 40%,#9a9a9a)"></div><a>RD3/4 200 karusel vrata</a></div>
  <div class="abs prod" style="left:228px"><div class="ph" role="img" aria-label="Photo of a warehouse loading dock with industrial doors" style="background:linear-gradient(180deg,#3d4250 0%,#5d6270 45%,#9aa0ab 100%)"></div><a>RD3/4 200 karusel vrata</a></div>
  <div class="abs prod" style="left:405px"><div class="ph" role="img" aria-label="Photo of a steel roller shutter door" style="background:linear-gradient(90deg,#8a7f7c,#bdbdbd 40%,#9a9a9a)"></div><a>RD3/4 200 karusel vrata</a></div>
</section>
<div class="abs blueline"></div>

<div class="abs card" style="left:148px;width:197px"><h4>Pretovarni mostovi</h4><p>u toku su radovi na novoj web prezent-aciji naših usluga, uskoro</p><small>VIEW PRODUCT</small></div>
<div class="abs card" style="left:357px;width:197px"><h4>Pretovarni mostovi</h4><p>u toku su radovi na novoj web prezent-aciji naših usluga, uskoro</p><small>VIEW PRODUCT</small></div>
<div class="abs news">
  <div class="meta">August 20, 2015 | On the News | Tarnwell Daily</div>
  <p>vorental on Tarnwell Daily: Hedge Funds Suddenly Find Real Money Is Back in Argentina's Debt</p>
  <small>By Lena Varga</small>
</div>

<div class="abs slider"><i></i><b></b></div>

<section class="abs partners">
  <h2>They trust our company!</h2>
  <div class="logos"><span>QUORVANE</span><span>TELMIRO</span><span>AVROSTIN</span><span>BRELLIX</span><span>Dunwake</span></div>
</section>

<footer>
  <div class="abs footer" style="left:148px;width:140px;text-align:center">
    <div class="brand" style="position:static;font-size:14px;justify-content:center;gap:6px"><span class="brand-mark" style="width:10px;height:10px"></span>vorental d.o.o.</div>
    <div style="margin-top:28px;color:#666;line-height:14.5px">© 2008-2016<br>Vorental d.o.o. Brelovo</div>
  </div>
  <div class="abs footer fcol" style="left:306px;padding-left:39px"><a>Company</a><a>Reference</a><a>Contact</a></div>
  <div class="abs footer fcol" style="left:449px;padding-left:40px"><a>Automatska Vrata</a><a>Industrijska Vrata</a><a>Rolo Vrata</a><a>Kontrola Pristupa</a></div>
  <div class="abs footer fcol contact" style="left:612px;padding-left:41px">
    <h5>CONTACT</h5>
    <div>Lipova Ulica 12,</div><div>71450 BRELOVO</div>
    <div style="font-weight:700">Call: +387 53 400 120</div>
    <div style="font-weight:700">Fax: +387 53 400 121</div>
  </div>
</footer>
</body>
</html>
```